need to look like a trust worthy company who help the public with technicial Problems

we need a digner who can create a company brochure for a company that specialize in installation, maintenance, repairs and cover for Televisions sets. We are unable to change our website which is very out dated and simple due to the banking regulations. So we require a brochure to inspire staff and customers bringing the company forward to 2016.

Target Market(s)

Home owners

Industry/Entity Type

It Company

Font styles to use
Serif

Requirements
Must have
• This is going to been seen like our website so it needs to look modern and clean. also needs a different vary of people in picture so young and old and different race. some nice family enjoying there TV it needs to look like we offer a service to everyone.
Nice to have

```html
<!DOCTYPE html>
<html lang="en">
<head>
<meta charset="utf-8">
<title>Clearview Specialist Solutions – Brochure</title>
<link rel="stylesheet" href="https://fonts.googleapis.com/css2?family=Raleway:wght@300;400;500&family=Open+Sans:wght@400;600;700&display=swap">
<style>
  :root{
    --blue:#1f6fba;
    --blue-deep:#155a9c;
    --blue-soft:rgba(31,111,186,.82);
    --paper:#f4f5f6;
    --paper-shade:#eceef0;
    --ink:#3c3f44;
    --ink-soft:#6a6e74;
    --stage:#e3e5e8;
    --white:#ffffff;
  }
  *{box-sizing:border-box;margin:0;padding:0}
  html,body{width:960px;height:1200px;overflow:hidden}
  body{background:var(--stage);font-family:"Open Sans",Arial,sans-serif;color:var(--ink);position:relative}

  .spread{position:absolute;left:30px;width:900px;height:318px;display:flex;box-shadow:0 6px 18px rgba(0,0,0,.12)}
  .spread--outside{top:232px}
  .spread--inside{top:650px}
  .page{position:relative;width:450px;height:318px;background:var(--paper);overflow:hidden}
  .page + .page{border-left:1px solid #d8dade}
  .page--left{background:linear-gradient(90deg,var(--paper) 85%,var(--paper-shade))}
  .page--right{background:linear-gradient(90deg,var(--paper-shade),var(--paper) 15%)}

  .display{font-family:"Raleway",Arial,sans-serif;font-weight:300;text-transform:uppercase;letter-spacing:.06em}

  /* Back cover */
  .back-band{position:absolute;left:0;top:0;width:450px;height:150px;background:var(--blue);clip-path:polygon(0 0,100% 0,100% 62%,0 100%)}
  .back-band__name{position:absolute;left:38px;top:30px;color:var(--white);font-size:13px}
  .back-band__contact{position:absolute;left:110px;top:60px;color:var(--white);font-size:6.5px;line-height:1.45}
  .back-band__contact p:last-child{margin-top:5px}

  /* Front cover */
  .cover-title{position:absolute;right:22px;top:40px;font-size:15px;color:#222}
  .cover-photo{position:absolute;left:0;top:118px;width:270px;height:200px;background:linear-gradient(135deg,#d9d2c8,#8a6a55 45%,#3b3f5a 80%,#2b3b6e);clip-path:polygon(0 0,100% 0,82% 100%,0 100%)}
  .cover-band{position:absolute;left:160px;top:190px;width:290px;height:74px;background:var(--blue-soft);clip-path:polygon(14% 0,100% 0,100% 100%,0 100%)}
  .cover-band__text{position:absolute;right:22px;top:12px;text-align:right;color:var(--white);font-size:15px;line-height:1.3}
  .cover-band__text strong{font-weight:400}
  .cover-url{position:absolute;right:24px;top:276px;font-size:7.5px;font-weight:600;color:var(--blue)}

  /* Inside left */
  .intro-band{position:absolute;left:0;top:26px;width:450px;height:52px;background:var(--blue)}
  .intro-band p{padding:11px 22px 0;color:var(--white);font-size:6.6px;line-height:1.5}
  .features{position:absolute;left:18px;top:94px;width:414px;display:grid;grid-template-columns:repeat(3,1fr);row-gap:10px;column-gap:10px}
  .feature{text-align:center}
  .feature__icon{display:block;margin:0 auto 5px;width:34px;height:34px}
  .feature__title{font-family:"Raleway",Arial,sans-serif;font-weight:400;font-size:8.5px;text-transform:uppercase;letter-spacing:.03em;color:#2c2f33;margin-bottom:3px}
  .feature__text{font-size:6px;line-height:1.45;color:var(--ink-soft);padding:0 6px}

  /* Inside right */
  .corner-tab{position:absolute;left:0;top:20px;width:130px;height:40px;background:var(--blue);clip-path:polygon(0 0,100% 0,86% 100%,0 100%)}
  .scene-photo{position:absolute;left:184px;top:12px;width:266px;height:178px;background:linear-gradient(120deg,#2d3e5a,#6d8fb8 30%,#c9a54a 48%,#e8eaee 62%,#c7b8a8 85%,#e8e9eb);clip-path:polygon(6% 0,100% 0,100% 100%,0 100%)}
  .service{position:absolute;left:16px;top:72px;width:158px;font-size:6.2px;line-height:1.5;color:var(--ink-soft)}
  .service ul{list-style:none;margin:5px 0 8px 6px;color:var(--blue);font-weight:700}
  .service p + p{margin-top:4px}
  .pricing{position:absolute;left:192px;top:190px;width:258px;height:96px;background:var(--blue);color:var(--white);padding:10px 14px;font-size:6.2px;line-height:1.5}
  .pricing__grid{display:flex;gap:30px;margin-top:8px}
</style>
</head>
<body>

<section class="spread spread--outside" aria-label="Brochure outside: back and front cover">
  <article class="page page--left back-cover">
    <div class="back-band">
      <h2 class="back-band__name display">Clearview Specialist Solutions</h2>
      <div class="back-band__contact">
        <p>14 Harbour Row<br>Eastmere-on-Sea<br>England<br>EM2 4QT</p>
        <p>T: 01632 960 418</p>
        <p>help@clearviewtvsolutions.co.uk</p>
      </div>
    </div>
  </article>

  <article class="page page--right front-cover">
    <h1 class="cover-title display">Clearview Specialist Solutions</h1>
    <div class="cover-photo" role="img" aria-label="Photo of a smiling family of four relaxing together on a sofa watching TV"></div>
    <div class="cover-band">
      <p class="cover-band__text display">Welcome to <strong>Clearview</strong><br>TV Experts</p>
    </div>
    <p class="cover-url">www.clearviewtvsolutions.co.uk</p>
  </article>
</section>

<section class="spread spread--inside" aria-label="Brochure inside spread">
  <article class="page page--left">
    <div class="intro-band">
      <p>Clearview Specialist Solutions LTD is a UK engineering firm (Clearview are not an insurance firm). Clearview is a network of engineers covering the whole of the UK. Clearview ensures that all its customers television sets are continuously working at its full potential during the length of their service agreement.</p>
    </div>

    <div class="features">
      <div class="feature">
        <svg class="feature__icon" viewBox="0 0 34 34" aria-hidden="true"><circle cx="17" cy="17" r="16" fill="none" stroke="var(--blue)" stroke-width="1.2"/><polygon points="17,8 19.6,14 26,14.4 21,18.6 22.6,25 17,21.5 11.4,25 13,18.6 8,14.4 14.4,14" fill="var(--blue)"/></svg>
        <h3 class="feature__title">Expert Service</h3>
        <p class="feature__text">Rest assured that our engineers are qualified to be working on your TV if failure occurs. Potential problems, and minor issues are dealt with on the spot.</p>
      </div>
      <div class="feature">
        <svg class="feature__icon" viewBox="0 0 34 34" aria-hidden="true"><circle cx="17" cy="17" r="16" fill="none" stroke="var(--blue)" stroke-width="1.2"/><path d="M12 9c1.5-.5 2.5 3 2 4l-1.5 1.2c.8 2.5 2.6 4.4 5 5.3l1.3-1.4c1-.5 4.4.6 4 2.2l-.7 2.4c-.4 1-1.6 1.4-2.8 1.1C13.8 22.4 10.5 18.8 9.4 13.4c-.2-1.2.3-2.4 1.3-3z" fill="var(--blue)"/></svg>
        <h3 class="feature__title">UK Based Call Centres</h3>
        <p class="feature__text">If you need any assistance with your TV, including setup, technical help and faults. Someone who can help is only a phone call away with our service.</p>
      </div>
      <div class="feature">
        <svg class="feature__icon" viewBox="0 0 34 34" aria-hidden="true"><circle cx="17" cy="17" r="16" fill="none" stroke="var(--blue)" stroke-width="1.2"/><rect x="11" y="8" width="11" height="15" rx="1" fill="none" stroke="var(--blue)" stroke-width="1.6"/><path d="M13.5 12h6M13.5 15h6M13.5 18h3" stroke="var(--blue)" stroke-width="1.2"/><path d="M17 23l3 3 6-7" fill="none" stroke="var(--blue)" stroke-width="2"/></svg>
        <h3 class="feature__title">All Costs Covered</h3>
        <p class="feature__text">Our repair costs are all inclusive, you will only ever pay the price you were quoted.</p>
      </div>
      <div class="feature">
        <svg class="feature__icon" viewBox="0 0 34 34" aria-hidden="true"><circle cx="17" cy="17" r="16" fill="none" stroke="var(--blue)" stroke-width="1.2"/><path d="M10 13.5h12M19 10.5l3.5 3-3.5 3M24 20.5H12M15 17.5l-3.5 3 3.5 3" fill="none" stroke="var(--blue)" stroke-width="2"/></svg>
        <h3 class="feature__title">Repair or Replace</h3>
        <p class="feature__text">If your TV cannot be repaired we can arrange to replace it with equipment of similar specification.</p>
      </div>
      <div class="feature">
        <svg class="feature__icon" viewBox="0 0 34 34" aria-hidden="true"><circle cx="17" cy="17" r="16" fill="none" stroke="var(--blue)" stroke-width="1.2"/><circle cx="17" cy="17" r="8" fill="none" stroke="var(--blue)" stroke-width="1.8"/><path d="M17 12v5l3.5 2" fill="none" stroke="var(--blue)" stroke-width="1.8"/></svg>
        <h3 class="feature__title">Agreed Repair Time Slots</h3>
        <p class="feature__text">We organise repairs or replacements at your convenience, making the whole repair process quick and easy.</p>
      </div>
      <div class="feature">
        <svg class="feature__icon" viewBox="0 0 34 34" aria-hidden="true"><circle cx="17" cy="17" r="16" fill="none" stroke="var(--blue)" stroke-width="1.2"/><path d="M17 8l8 3v5.5c0 4.6-3.3 8.2-8 9.5-4.7-1.3-8-4.9-8-9.5V11z" fill="var(--blue)"/><path d="M13.5 17l2.5 2.5 4.5-5" fill="none" stroke="var(--white)" stroke-width="1.6"/></svg>
        <h3 class="feature__title">Accidental Damage</h3>
        <p class="feature__text">Accidents happen, we will repair your TV under these circumstances, give us a call to discuss our services.</p>
      </div>
    </div>
  </article>

  <article class="page page--right">
    <div class="corner-tab"></div>
    <div class="scene-photo" role="img" aria-label="Photo of a couple in a bright living room pointing at a wall-mounted smart TV showing its home screen"></div>

    <div class="service">
      <p>The service Clearview provides, is a fully comprehensive coverage for the following:</p>
      <ul>
        <li>Television set</li>
        <li>Power cable</li>
        <li>Remote control</li>
        <li>Over the phone technical support</li>
      </ul>
      <p>Engineer callouts and if the television set is deemed beyond economical repair, we will replace it like for like.</p>
      <p>95% of people already have a cover and can be paying up to around £170 per year and on some occasions more and they haven't made a claim in the last 12 months.</p>
      <p>Clearview aims to switch the customers onto a cheaper policy with up to 50% savings. At the same time Clearview provide the same level of service, that the customers are currently paying for, at a fraction of the cost. This is the reason this product is so desirable and easy to sell. It is company policy to comply all sales after a 24 hour cooling off period.</p>
    </div>

    <div class="pricing">
      <p>Below is the pricing for Clearview services. Clearview understand different customers have different needs, because of this we have a variety of different policies and we can also provide payment plans suitable for all customers.</p>
      <div class="pricing__grid">
        <p>2 year policy: £170<br>2 year policy + 1 extra TV: £240<br>2 year policy: £85x2<br>2 year policy: £45x4</p>
        <p>1 year policy: £90<br>1 year policy: £45x2<br>1 year policy + 1 extra TV: £140</p>
      </div>
    </div>
  </article>
</section>

</body>
</html>
```